business card for retail pharmacy
Brookfield Pharmacy
Project: business card for retail pharmacy
business card for retail pharmacy - Pharmacy/Pharmaceuticals
Creative Brief
Simple
Gerald P. Ostrander RPh
Owner/Pharmacist
4217 Route 531, Unit #3, Southampton, NJ 08088
brookrxcare7@mailvessel.com
www.brookfieldrxnj-example.com
Hours Monday-Friday 9-7, Saturday 9-1
brookrxcare7 brookrxcare7
Would like to see some cards as red and blue NOT red and gray. We are still not finalized on the logo colors so I would like to see as a red and dark ble combination.
Plidor Plidor

```html
<!DOCTYPE html>
<html lang="en">
<head>
<meta charset="utf-8">
<title>Brookfield Pharmacy – Business Card</title>
<link href="https://fonts.googleapis.com/css2?family=Oswald:wght@400;500;600&family=Roboto:wght@400;500&display=swap" rel="stylesheet">
<style>
  :root {
    --backdrop: #e9e6e2;
    --card-white: #fbfbfb;
    --card-mist: #eeeeee;
    --brand-red: #d7262d;
    --brand-red-dark: #b81c22;
    --brand-red-light: #e23a40;
    --navy: #14284b;
    --navy-deep: #0c1a33;
    --navy-light: #1f3a66;
    --text-white: #ffffff;
    --text-pale: #c9d4e8;
    --icon-ring: rgba(255,255,255,0.9);
  }
  * { box-sizing: border-box; margin: 0; padding: 0; }
  html, body {
    width: 1200px; height: 768px; overflow: hidden;
    background: var(--backdrop);
  }
  .business-card {
    position: absolute; left: 150px; top: 127px;
    width: 900px; height: 514px;
    border-radius: 6px; overflow: hidden;
    box-shadow: 0 18px 40px rgba(0,0,0,0.18);
    font-family: "Roboto", sans-serif;
  }
  .brand-area {
    height: 205px;
    background: linear-gradient(90deg, var(--card-mist) 0%, var(--card-white) 45%, var(--card-mist) 100%);
    display: flex; align-items: center; justify-content: center;
  }
  .brand-name {
    font-family: "Oswald", sans-serif; font-weight: 600;
    color: var(--brand-red);
    font-size: 46px; letter-spacing: 2px; text-transform: uppercase;
    display: flex; align-items: center; gap: 16px;
  }
  .brand-mark {
    width: 22px; height: 22px; border-radius: 50%;
    background: var(--navy);
  }
  .contact-band {
    position: relative; height: 240px;
    background: linear-gradient(100deg, var(--brand-red-dark) 0%, var(--brand-red) 40%, var(--brand-red-light) 70%, var(--brand-red-dark) 100%);
    border-top: 4px solid var(--navy);
  }
  .contact-item {
    position: absolute; top: 24px;
    transform: translateX(-50%);
    display: flex; flex-direction: column; align-items: center;
    color: var(--text-white); text-align: center;
  }
  .contact-item.person { left: 18%; }
  .contact-item.online { left: 50%; }
  .contact-item.phone  { left: 83%; }
  .icon-ring {
    width: 64px; height: 64px; border-radius: 50%;
    background: var(--icon-ring);
    display: flex; align-items: center; justify-content: center;
    margin-bottom: 16px;
  }
  .icon-ring svg { width: 36px; height: 36px; }
  .person-name {
    font-family: "Oswald", sans-serif; font-weight: 500;
    font-size: 28px; line-height: 1.15; text-transform: uppercase; white-space: nowrap;
  }
  .person-credential { font-size: 18px; font-weight: 400; margin-left: 4px; }
  .person-role {
    font-size: 13px; letter-spacing: 1.5px; text-transform: uppercase; margin-top: 6px;
  }
  .contact-line { font-size: 17px; line-height: 1.5; white-space: nowrap; }
  .follow-band {
    height: 66px;
    background: linear-gradient(180deg, var(--navy-light) 0%, var(--navy) 50%, var(--navy-deep) 100%);
    display: flex; align-items: center; padding-left: 84px;
  }
  .follow-label {
    font-family: "Oswald", sans-serif; color: var(--text-white);
    font-size: 22px; letter-spacing: 1px; line-height: 1; width: 220px;
  }
  .follow-label small {
    display: block; font-family: "Roboto", sans-serif;
    font-size: 9px; letter-spacing: 1px; color: var(--text-pale); margin-top: 3px;
  }
  .social-list { display: flex; gap: 26px; list-style: none; }
  .social-list li {
    font-family: "Oswald", sans-serif; font-weight: 500;
    font-size: 15px; color: var(--text-white);
  }
</style>
</head>
<body>
  <article class="business-card">
    <header class="brand-area">
      <div class="brand-name"><span class="brand-mark"></span>Brookfield Pharmacy</div>
    </header>

    <section class="contact-band">
      <div class="contact-item person">
        <div class="icon-ring">
          <svg viewBox="0 0 40 40" aria-hidden="true">
            <circle cx="20" cy="13" r="7" fill="#14284b"/>
            <path d="M6 36 C6 26 12 22 20 22 C28 22 34 26 34 36 Z" fill="#14284b"/>
          </svg>
        </div>
        <div class="person-name">Gerald P. Ostrander<span class="person-credential">RPh</span></div>
        <div class="person-role">Owner / Pharmacist</div>
      </div>

      <div class="contact-item online">
        <div class="icon-ring">
          <svg viewBox="0 0 40 40" aria-hidden="true" fill="none" stroke="#14284b" stroke-width="2.4">
            <circle cx="20" cy="20" r="16"/>
            <ellipse cx="20" cy="20" rx="7" ry="16"/>
            <line x1="4" y1="20" x2="36" y2="20"/>
            <path d="M7 11 H33 M7 29 H33"/>
          </svg>
        </div>
        <div class="contact-line">brookrxcare7@mailvessel.com</div>
        <div class="contact-line">www.brookfieldrxnj-example.com</div>
        <div class="contact-line">4217 Route 531, Unit #3</div>
        <div class="contact-line">Southampton, NJ 08088</div>
      </div>

      <div class="contact-item phone">
        <div class="icon-ring">
          <svg viewBox="0 0 40 40" aria-hidden="true">
            <rect x="11" y="3" width="18" height="34" rx="3" fill="#14284b"/>
            <rect x="14" y="8" width="12" height="22" fill="#ffffff"/>
            <circle cx="20" cy="33" r="1.8" fill="#ffffff"/>
          </svg>
        </div>
        <div class="contact-line">609 555 0142</div>
        <div class="contact-line">Mon–Fri 9–7</div>
        <div class="contact-line">Saturday 9–1</div>
      </div>
    </section>

    <footer class="follow-band">
      <div class="follow-label">FOLLOW US<small>ON SOCIAL NETWORKS</small></div>
      <ul class="social-list">
        <li>Chirpa</li>
        <li>Frendo</li>
        <li>Workly</li>
        <li>Callvo</li>
      </ul>
    </footer>
  </article>
</body>
</html>
```